BKA

Please send us some options for letterhead I attached our Logo. In addition to the Logo we need this information somewhere on the page

47 Fenbury Lane
Larkfield, ME 04190
555-481-7629

```html
<!DOCTYPE html>
<html lang="en">
<head>
<meta charset="utf-8">
<title>BKA Letterhead</title>
<link href="https://fonts.googleapis.com/css2?family=Open+Sans:wght@400;600&display=swap" rel="stylesheet">
<style>
  :root {
    --backdrop: #ececec;
    --paper: #ffffff;
    --brand-brown: #5d5352;
    --brand-blue: #3f8fd2;
    --body-text: #6a6a6a;
    --rule-dark: #4a4342;
    --signature-tone: #efefef;
  }
  * { margin: 0; padding: 0; box-sizing: border-box; }
  html, body {
    width: 1200px; height: 1000px; overflow: hidden;
    background: var(--backdrop);
    font-family: "Open Sans", Arial, sans-serif;
  }
  .letterhead {
    position: absolute; left: 282px; top: 50px;
    width: 636px; height: 900px;
    background: var(--paper);
    box-shadow: 0 2px 10px rgba(0,0,0,0.08);
    padding: 0 78px;
  }
  .brand {
    display: flex; align-items: center; justify-content: center;
    gap: 10px; margin-top: 70px;
  }
  .brand-mark { width: 30px; height: 30px; background: var(--brand-brown); }
  .brand-name {
    font-size: 30px; font-weight: 600; letter-spacing: 2px;
    color: var(--brand-brown);
  }
  .letter-body {
    margin-top: 48px;
    font-size: 10.5px; line-height: 1.55;
    color: var(--body-text);
  }
  .letter-body p { margin-bottom: 26px; text-align: justify; }
  .letter-body .salutation { margin-bottom: 12px; }
  .letter-body .closing { margin-bottom: 12px; }
  .signature {
    width: 150px; height: 56px;
    background: var(--signature-tone);
    border-radius: 4px;
  }
  .letter-footer {
    position: absolute; left: 78px; right: 78px; bottom: 56px;
    text-align: center;
  }
  .contact-line {
    display: inline-flex; align-items: center; gap: 8px;
    font-size: 13px; color: var(--brand-brown);
  }
  .contact-line .marker { width: 14px; height: 14px; background: var(--brand-blue); }
  .contact-line .divider { color: var(--brand-blue); }
  .footer-rule {
    height: 4px; background: var(--rule-dark);
    margin: 8px auto 0; width: 270px;
  }
</style>
</head>
<body>
  <main class="letterhead">
    <header class="brand">
      <span class="brand-mark"></span>
      <span class="brand-name">BKA</span>
    </header>

    <section class="letter-body">
      <p class="salutation">Dear Client,</p>
      <p>Lorem ipsum dolor sit amet, consectetur adipiscing elit. Nulla sodales nisi vitae lorem ipsum dolor sit amet, consectetur adipiscing elit. Suspendisse feugiat eros nisi, a facilisis risus eleifend sed. Aliquam mauris enim, fermentum eu lacinia sit amet, laoreet eu leo. Nullam eleifend nulla in libero tristique, ac vulputate odio tincidunt. Etiam non condimentum tortor. Integer suscipit neque nec odio porttitor cursus. Phasellus a sapien blandit, suscipit justo id, condimentum ante. Morbi tristique justo risus, id mattis dui molestie ut. Nullam volutpat ut quam commodo faucibus. Pellentesque urna est, interdum in elit quis, pharetra elementum orci. Nam pharetra velit molestie justo placerat scelerisque.</p>
      <p>Nulla tincidunt molestie libero vel pretium. Donec condimentum nulla sit amet risus semper imperdiet. Duis congue eros nec diam blandit, et pellentesque sapien auctor. Curabitur iaculis enim lectus, in imperdiet mauris mattis eget. Etiam ac ornare metus. Mauris risus leo, egestas at dolor a, ultrices adipiscing est. Nunc faucibus scelerisque mollis. Pellentesque aliquet mauris tellus, id dignissim risus viverra et. Mauris venenatis lobortis eros. Nam id diam in ligula malesuada feugiat. Cras turpis felis, aliquet id mauris elementum, feugiat ultricies nisl.</p>
      <p>Nullam auctor venenatis metus, eu pulvinar sapien dapibus non. Cum sociis natoque penatibus et magnis dis parturient montes, nascetur ridiculus mus. Praesent sed lorem eget tortor volutpat dictum vel vel ipsum. Morbi ac mauris sed elit dictum volutpat. Morbi pulvinar non nisi in ultrices. Pellentesque quis mi in risus eleifend adipiscing.</p>
      <p class="closing">Best regards,</p>
      <div class="signature" role="img" aria-label="Handwritten signature of the sender"></div>
    </section>

    <footer class="letter-footer">
      <div class="contact-line">
        <span class="marker"></span>
        <span class="address">47 Fenbury Lane Larkfield, ME 04190</span>
        <span class="divider">|</span>
        <span class="phone">555-481-7629</span>
      </div>
      <div class="footer-rule"></div>
    </footer>
  </main>
</body>
</html>
```